Charity fundraising company - need eDM design!

We are a telemarketing company working with charities to raise money from individuals via regular monthly direct debits or credit card payments. The audience for this eDM is a few hundred fundraising managers. We want to provide a clearly laid-out email to deliver our offer of a free telemarketing consultation.

The eDM will be sent via Mailchimp.

Industry/Entity Type

Charity

Logo Text

KELP Dial

Font styles to use
Sans Serif
Other font styles liked:
• Helvetica Neue

Requirements
Nice to have
• Our values:
• Storytelling with passion
• Fundraising with integrity
• Results that deliver a strong return on your charity's investment.
Should not have
• Logo at the top of the eDM (please place at the bottom)

```html
<!DOCTYPE html>
<html lang="en">
<head>
<meta charset="utf-8">
<title>KELP Dial – Complimentary Tele-Fundraising Consultation</title>
<link rel="stylesheet" href="https://fonts.googleapis.com/css2?family=Open+Sans:ital,wght@0,400;1,400&family=Source+Sans+3:wght@400;600;700&display=swap">
<style>
  :root {
    --page-bg: #e9e9e9;
    --card-bg: #ffffff;
    --brand-red: #d91f26;
    --rule-red: #b0202a;
    --ink: #1d1d1d;
    --ink-soft: #3a3a3a;
    --muted: #7a7a7a;
    --photo-grey-light: #d6d6d6;
    --photo-grey-dark: #8e8e8e;
    --photo-night: #1f2226;
    --photo-warm: #4a3a30;
    --social: #555a60;
  }
  * { box-sizing: border-box; margin: 0; padding: 0; }
  html, body { width: 1081px; height: 1200px; overflow: hidden; }
  body {
    background: var(--page-bg);
    font-family: "Source Sans 3", "Helvetica Neue", Arial, sans-serif;
    color: var(--ink);
    position: relative;
  }
  .preheader {
    position: absolute; top: 100px; left: 0; width: 100%;
    text-align: center;
    font-family: "Open Sans", Arial, sans-serif;
    font-size: 16px; color: var(--ink);
  }
  .preheader a { color: var(--brand-red); font-style: italic; }
  .card {
    position: absolute; left: 174px; top: 151px;
    width: 732px; height: 899px;
    background: var(--card-bg);
    border-top: 6px solid var(--rule-red);
    border-bottom: 6px solid var(--rule-red);
  }
  .hero-photo { position: absolute; top: 140px; height: 148px; }
  .hero-photo--headset {
    left: 68px; width: 372px;
    background: linear-gradient(120deg, var(--photo-grey-light), var(--photo-grey-dark));
  }
  .hero-photo--agent {
    left: 444px; width: 221px;
    background: radial-gradient(circle at 55% 45%, var(--photo-warm), var(--photo-night) 70%);
  }
  .headline {
    position: absolute; top: 314px; left: 67px;
    font-size: 27px; font-weight: 400; color: var(--ink);
  }
  .subhead {
    position: absolute; top: 368px; left: 68px;
    font-size: 19px; font-weight: 600; color: var(--ink-soft);
  }
  .intro, .lead-in {
    position: absolute; left: 68px; width: 586px;
    font-size: 14.6px; line-height: 22px; color: var(--ink-soft);
  }
  .intro { top: 404px; }
  .lead-in { top: 456px; }
  .offer-list { position: absolute; top: 488px; left: 84px; width: 520px; list-style: none; }
  .offer-list li {
    position: relative; padding-left: 26px;
    font-size: 14.6px; line-height: 22px; color: var(--ink-soft);
    margin-bottom: 6px;
  }
  .offer-list li.spaced { margin-top: 20px; }
  .offer-list svg { position: absolute; left: 0; top: 6px; }
  .cta {
    position: absolute; top: 732px; left: 210px; width: 314px; height: 61px;
    background: var(--brand-red); color: #fff; text-align: center;
    text-decoration: none;
    border-radius: 2px; padding-top: 10px;
  }
  .cta strong { display: block; font-size: 15.5px; font-weight: 700; letter-spacing: .2px; line-height: 20px; }
  .cta span { display: block; font-size: 15.5px; line-height: 20px; }
  .contact-link {
    position: absolute; top: 806px; left: 0; width: 100%; text-align: center;
    font-size: 14.6px; color: var(--ink);
  }
  .contact-link a { color: var(--ink); }
  .social { position: absolute; top: 840px; left: 317px; display: flex; gap: 5px; }
  .social span { width: 29px; height: 29px; border-radius: 50%; background: var(--social); }
  .wordmark-foot {
    position: absolute; top: 848px; left: 592px;
    font-size: 13px; font-weight: 600; letter-spacing: 2px; color: var(--muted);
  }
</style>
</head>
<body>
  <p class="preheader">For anything about this mail you can contract us by <a href="#">click this link.</a></p>

  <main class="card">
    <div class="hero-photo hero-photo--headset" role="img" aria-label="Photo of a black call-centre headset on a grey surface"></div>
    <div class="hero-photo hero-photo--agent" role="img" aria-label="Photo of a smiling call-centre agent wearing a headset"></div>

    <h1 class="headline">Complimentary Tele-Fundraising Consultation</h1>
    <h2 class="subhead">Want more regular givers for your cause?</h2>
    <p class="intro">KELP Dial is Australia’s leading telemarketing specialist for acquiring new regular givers through lead generation.</p>
    <p class="lead-in">Speak to us today and we will:</p>

    <ul class="offer-list">
      <li><svg width="12" height="10" viewBox="0 0 12 10"><path d="M1 5l3.5 3.5L11 1" fill="none" stroke="#555" stroke-width="1.6"/></svg>Run a no-obligation TM donor acquisition feasibility assessment for you</li>
      <li><svg width="12" height="10" viewBox="0 0 12 10"><path d="M1 5l3.5 3.5L11 1" fill="none" stroke="#555" stroke-width="1.6"/></svg>Offer a Cost Per Acquisition model, with a sliding scale of fees based on the volume of leads provided</li>
      <li><svg width="12" height="10" viewBox="0 0 12 10"><path d="M1 5l3.5 3.5L11 1" fill="none" stroke="#555" stroke-width="1.6"/></svg>Handle the entire data ordering and management process for you at no additional cost</li>
      <li class="spaced"><svg width="12" height="10" viewBox="0 0 12 10"><path d="M1 5l3.5 3.5L11 1" fill="none" stroke="#555" stroke-width="1.6"/></svg>Whether you currently run a phone acquisition campaignand would like to increase your ROI, or you’re simply interested in exploring how thistype of campaign might work for your cause, drop us a line today</li>
    </ul>

    <a class="cta" href="#"><strong>FREE NO-OBLIGATION CONSULTATION</strong><span>Drop us a line today…</span></a>

    <p class="contact-link"><a href="#">http://kelpdial.com/contact-us/</a></p>

    <div class="social" aria-label="Social links"><span></span><span></span><span></span></div>

    <div class="wordmark-foot">KELP DIAL</div>
  </main>
</body>
</html>
```